Website redesign

Looking to redesign our existing website. (quill7meadows.com.au)
New design needs to be bright, fun and have an easy flowing.
The website needs to be design with call to action.

Some examples of other websites:
fernquaylo.com
tovanmilk.com.au

We are happy with the content of our existing website.

Target Market(s)

other businesses

Industry/Entity Type

Business Service

Number of Pages Required

5+ page

Requirements
Must have
• Theme redesign
Cool animation similar to fernquaylo.com

```html
<!DOCTYPE html>
<html lang="en">
<head>
<meta charset="utf-8">
<title>Quill 7 Meadows – Virtual Assistants</title>
<link rel="stylesheet" href="https://fonts.googleapis.com/css2?family=Poppins:wght@300;400;500;600;700;800&display=swap">
<style>
  :root{
    --blue:#1ea7e1;
    --blue-dark:#1583c4;
    --ink:#2b2b33;
    --muted:#8a8f99;
    --hero-bg:#f2f6fb;
    --card-bg:#ffffff;
    --step-bg:#f5f5f7;
    --white:#ffffff;
  }
  *{box-sizing:border-box;margin:0;padding:0}
  html,body{width:1200px;height:3413px;overflow:hidden}
  body{position:relative;font-family:'Poppins',sans-serif;color:var(--ink);background:var(--white)}
  .abs{position:absolute}
  a{color:inherit;text-decoration:none}

  /* header */
  .site-header{position:absolute;left:0;top:0;width:1200px;height:93px;background:var(--white)}
  .brand{position:absolute;left:126px;top:30px;display:flex;align-items:center;gap:6px;font-weight:600;font-size:12px;color:var(--ink)}
  .brand-dot{width:10px;height:10px;border-radius:50%;background:var(--blue)}
  .main-nav a{position:absolute;top:36px;font-size:12px;font-weight:600;color:var(--ink)}
  .main-nav a.active{color:var(--blue)}
  .main-nav a.active::after{content:"";position:absolute;left:0;right:0;bottom:-7px;height:2px;background:var(--blue)}
  .btn-register{position:absolute;left:995px;top:29px;width:79px;height:32px;border-radius:16px;background:var(--blue);color:var(--white);font-size:10px;font-weight:600;display:flex;align-items:center;justify-content:center}

  /* hero */
  .hero{position:absolute;left:0;top:93px;width:1200px;height:583px;background:var(--hero-bg)}
  .eyebrow{left:126px;top:131px;font-size:10px;font-weight:600;color:var(--blue);letter-spacing:.1px}
  .hero-title{left:126px;top:153px;font-size:39px;line-height:54px;font-weight:800;color:var(--ink)}
  .hero-copy{left:126px;top:321px;width:420px;font-size:13px;line-height:25px;color:var(--ink)}
  .btn-start{left:126px;top:402px;width:176px;height:49px;border-radius:25px;background:var(--blue);color:var(--white);font-size:12px;font-weight:600;display:flex;align-items:center;padding-left:32px;gap:26px}
  .hero-art{left:550px;top:132px;width:523px;height:358px;border-radius:46% 40% 30% 50%/40% 45% 30% 55%;background:linear-gradient(135deg,#d9eefb,#b7def5 60%,#e4f3fc)}

  /* section heads */
  .sec-title{left:0;width:1200px;text-align:center;font-size:25px;font-weight:700}
  .sec-sub{left:150px;width:900px;text-align:center;font-size:14px;line-height:25px;color:var(--muted);font-weight:300}

  /* service cards */
  .service-card{top:960px;width:224px;height:195px;background:var(--card-bg);border-radius:14px;box-shadow:0 14px 30px rgba(40,60,90,.08);text-align:center}
  .service-card svg{position:absolute;left:90px;top:20px}
  .service-card p{position:absolute;left:10px;right:10px;top:110px;font-size:13px;line-height:20px;font-weight:500}

  /* video */
  .video-band{left:0;top:1448px;width:1200px;height:433px;background:linear-gradient(90deg,#5ba8d8,#2f86cc 45%,#2f7fc4 70%,#3c8fd0)}
  .play-outer{left:510px;top:1572px;width:186px;height:186px;border-radius:50%;background:rgba(255,255,255,.12)}
  .play-inner{left:542px;top:1604px;width:122px;height:122px;border-radius:50%;background:rgba(255,255,255,.2)}

  /* process */
  .step-band{left:205px;top:2195px;width:788px;height:361px;background:var(--step-bg);border-radius:20px}
  .step{position:absolute;text-align:center}
  .step h3{font-size:22px;font-weight:700;color:var(--blue);display:inline-block;padding-bottom:3px;border-bottom:2px solid var(--blue)}
  .step h4{margin-top:16px;font-size:15px;line-height:18px;font-weight:600}
  .step p{margin-top:28px;font-size:11px;line-height:20px;font-weight:500;color:#444}
  .step-feature{left:460px;top:2176px;width:278px;height:468px}
  .step-feature svg.shape{position:absolute;left:0;top:0;filter:drop-shadow(0 18px 24px rgba(40,60,90,.12))}
  .stars{display:inline-block;margin-top:40px;width:80px;height:20px;border-radius:10px;background:var(--blue);color:#ffd54a;font-size:10px;line-height:20px;letter-spacing:1px}
  .read-more{display:block;margin:9px auto 0;width:56px;font-size:10px;font-weight:600;border-bottom:1px solid var(--ink);padding-bottom:2px}
  .arrow{width:18px;height:30px}

  /* newsletter */
  .news-band{left:0;top:2720px;width:1200px;height:350px;background:linear-gradient(90deg,#5cb6e6,#7cc8ee 50%,#49a7df)}
  .news-box{left:294px;top:2781px;width:611px;height:230px;border-radius:18px;background:rgba(255,255,255,.25);text-align:center}
  .news-box h2{margin-top:32px;font-size:29px;font-weight:700;letter-spacing:1.5px;color:#2c3440}
  .news-box .lead{margin-top:6px;font-size:20px;letter-spacing:1px;color:#2c3440}
  .news-input{left:347px;top:2938px;width:376px;height:45px;background:var(--white);color:#b7bcc4;font-size:15px;padding-left:21px;line-height:45px;opacity:.9}
  .news-btn{left:723px;top:2938px;width:129px;height:45px;background:var(--blue);color:var(--white);font-size:15px;font-weight:700;text-align:center;line-height:45px}

  /* footer */
  .foot-brand{left:119px;top:3170px;font-size:19px;font-weight:500;display:flex;align-items:center;gap:8px}
  .foot-col h5{font-size:10px;font-weight:700;margin-bottom:16px}
  .foot-col a{display:block;font-size:12px;color:var(--muted);margin-bottom:10px}
  .call{right:140px;top:3155px;text-align:right;font-weight:700}
  .call .label{font-size:29px}
  .call .num{font-size:29px;margin-top:2px}
  .copyright{left:0;width:1200px;top:3374px;text-align:center;font-size:10px;color:#c4c7cd}
</style>
</head>
<body>

<header class="site-header">
  <a class="brand" href="#"><span class="brand-dot"></span>Quill 7 Meadows</a>
  <nav class="main-nav">
    <a class="active" href="#" style="left:439px">Home</a>
    <a href="#" style="left:526px">Our Story</a>
    <a href="#" style="left:636px">Tips And Tricks</a>
    <a href="#" style="left:779px">FAQ</a>
    <a href="#" style="left:856px">Contact US</a>
  </nav>
  <a class="btn-register" href="#">REGISTER</a>
</header>

<section class="hero">
  <div class="abs eyebrow">FULL TIME VIRTUAL ASSISTANT YOU BUSINESS</div>
  <h1 class="abs hero-title">VIRTUAL ASSISTANT?<br>MORE LIKE VALUABLE<br>ASSET!</h1>
  <p class="abs hero-copy">One invoice a month-no sneaky super or TAX! Tech nerds on standby for setup, support and comms!</p>
  <a class="abs btn-start" href="#">GET STARTED
    <svg width="8" height="12" viewBox="0 0 8 12"><path d="M1 1l5 5-5 5" fill="none" stroke="#fff" stroke-width="1.6"/></svg></a>
  <div class="abs hero-art" role="img" aria-label="Illustration of a virtual assistant at a large monitor with two colleagues working on laptops"></div>
</section>

<h2 class="abs sec-title" style="top:782px">Our Service</h2>
<p class="abs sec-sub" style="top:824px">We'll help you save tens (or even hundreds!) of thousands of dollars per year. But what do WE actually do?<br>GLAD YOU ASKED!</p>

<div class="abs service-card" style="left:126px">
  <svg width="44" height="44" viewBox="0 0 44 44" fill="none" stroke="#222" stroke-width="2"><circle cx="18" cy="18" r="15"/><path d="M29 29l12 12"/><circle cx="18" cy="14" r="4" fill="#222"/><path d="M10 26c2-5 14-5 16 0" fill="#222"/></svg>
  <p>We recruit Virtual&nbsp; Assistants (a.k.a office legends!), and</p>
</div>
<div class="abs service-card" style="left:366px">
  <svg width="44" height="44" viewBox="0 0 44 44" fill="none" stroke="#222" stroke-width="2"><circle cx="20" cy="12" r="7"/><path d="M6 40c0-10 8-15 14-15"/><rect x="20" y="28" width="20" height="12" rx="1" fill="#cfe3f5"/></svg>
  <p>Provide the tech support<br>for these superheroes!</p>
</div>
<div class="abs service-card" style="left:605px">
  <svg width="44" height="44" viewBox="0 0 44 44" fill="none" stroke="#1f5f9c" stroke-width="2.2"><rect x="2" y="8" width="40" height="30" rx="2"/><circle cx="14" cy="20" r="4"/><path d="M7 32c1-5 13-5 14 0M26 18h10M26 24h10M26 30h6"/></svg>
  <p>Set up the phone system<br>(their own Bat Phone!)</p>
</div>
<div class="abs service-card" style="left:845px">
  <svg width="44" height="44" viewBox="0 0 44 44" fill="none" stroke="#4b4fb5" stroke-width="2.2"><path d="M30 40H4V6h8"/><path d="M10 6v30"/><path d="M36 4l6 6-16 16h-6v-6z"/></svg>
  <p style="top:100px">We manage Virtual Assistants and keep them in tip-top shape!</p>
</div>

<h2 class="abs sec-title" style="top:1291px">Outsourcing. A big word that means big things for your business.</h2>
<p class="abs sec-sub" style="top:1332px;left:130px;width:940px">Virtual Assistants are the superheroes of the modern office. They can do everything your team can do on a computer at a fraction of the price! (Well, maybe not high five you when you've had a win, but a virtual high five is definitely on the table!)</p>

<div class="abs video-band" role="img" aria-label="Video still of two team members talking, tinted blue"></div>
<div class="abs play-outer"></div>
<div class="abs play-inner"></div>
<svg class="abs" style="left:588px;top:1646px" width="34" height="38" viewBox="0 0 34 38"><path d="M2 2l30 17L2 36z" fill="#fff"/></svg>

<h2 class="abs sec-title" style="top:1986px">The Process</h2>
<p class="abs sec-sub" style="top:2028px">Your Magical Journey Begins</p>

<svg class="abs arrow" style="left:110px;top:2348px" viewBox="0 0 18 30"><path d="M15 2L3 15l12 13" fill="none" stroke="#1ea7e1" stroke-width="3"/></svg>
<svg class="abs arrow" style="left:1054px;top:2348px" viewBox="0 0 18 30"><path d="M3 2l12 13L3 28" fill="none" stroke="#1ea7e1" stroke-width="3"/></svg>

<div class="abs step-band"></div>
<div class="step" style="left:225px;top:2236px;width:230px">
  <h3>Step 1</h3>
  <h4>Provide Your Preferred<br>Qualifications.</h4>
  <p>Set up a call with our team to specify the requirements and qualifications you're searching for in a Virtual Assistant. This will be our checklist for your perfect assistant! From there, we'll take care of shortlisting, testing, background checking and recruiting.</p>
</div>
<div class="step" style="left:750px;top:2236px;width:222px">
  <h3>Step 3</h3>
  <h4>Conducting the<br>Final Interview</h4>
  <p>The final interview is the perfect time to get to know the candidates. It'll help to have a list of questions prepared that will help you pick out the chosen one!</p>
</div>

<div class="abs step-feature">
  <svg class="shape" width="278" height="468" viewBox="0 0 278 468"><path d="M20 1h238a19 19 0 0 1 19 19v370L139 467 1 390V20A19 19 0 0 1 20 1z" fill="#fff" stroke="#d7d9de"/></svg>
  <div class="step" style="left:22px;top:60px;width:234px">
    <h3>Step 2</h3>
    <h4>Endorsing the<br>Shortlisted Candidates</h4>
    <p>After the thorough vetting process, we'll put forward the best candidate. You can then conduct the final interview on your preferred communication platform at a time that suits you. Once the schedule is set, we'll let the candidates know!</p>
    <span class="stars">★★★★★</span>
    <a class="read-more" href="#">Read More</a>
  </div>
</div>

<div class="abs news-band" role="img" aria-label="Photo of a team working at laptops in an office, tinted light blue"></div>
<div class="abs news-box">
  <h2>SUBSCRIBE OUR NEWALETTER</h2>
  <p class="lead">Receive Great Deal of Meadowtrade</p>
</div>
<div class="abs news-input">Your Email Address</div>
<div class="abs news-btn">SUBSCRIBE</div>

<footer>
  <div class="abs foot-brand"><span class="brand-dot" style="width:14px;height:14px"></span>QUILL 7 MEADOWS</div>
  <div class="abs foot-col" style="left:469px;top:3164px">
    <h5>ABOUT</h5><a href="#">About</a><a href="#">Fees</a><a href="#">Careers</a>
  </div>
  <div class="abs foot-col" style="left:634px;top:3164px">
    <h5>HELP</h5><a href="#">Customer Care</a><a href="#">Contact US</a><a href="#">Security Center</a>
  </div>
  <div class="abs call"><div class="label">Call Us</div><div class="num">07 5550 1946</div></div>
  <div class="abs copyright">All Rights Reserved 2020</div>
</footer>

</body>
</html>
```